Design a website for our "Bright Stride" Initiative we are implementing at our Youth Soccer Club.

We need a web design for a wellness initiative for our soccer club. "Bright Stride" is the program title. The website will have health and wellness content related to our initiative. It should have interactive features for our users. Videos, survey/data submission capabilities, etc. Colors themed to align with logo. see my start of a website at www.brightstridewithtown.example. I like the homepage design, the rest is unprofessional looking. Design should provide education, tips, advice, resources, for health & wellness; wellness related to our pillars. 6 tabs in addition to home page: Drink more water, fuel your performance, stretch more, protect your skin more, move more, and sports mindset. (year 2 diagram wheel). Sports counseling will be next big focus. Wordpress based website. Easy for me to update in the future.

Target Market(s)

Families with children participating in soccer. concept also applicable to other youth sports.

Industry/Entity Type

Health And Wellness

Number of Pages Required

5+ page

Font styles to use
Sans Serif

Colors
0292cd
f37122

Requirements
Must have
• Bright Stride Logo
• Marrowby Field Soccer Club Logo (*updated*)
• Home page
• Video included that is currently on the website homepage www.brightstridewithtown.example
• Page for each of the 6 pillars
• Focus on "drink more water" pillar and "Mindset" (will focus on sports counseling)
• Flexibility for me to update/edit the website moving forward (non-coding).
• User friendly graphic/picture interface
Nice to have
• Design focused more on the themes, not on soccer. Want the design to be applicable to parents and youth of all sports. Education and interactive features to all ages.

```html
<!DOCTYPE html>
<html lang="en">
<head>
<meta charset="utf-8">
<title>Bright Stride</title>
<link href="https://fonts.googleapis.com/css2?family=Roboto:wght@400;500;700&family=Oswald:wght@500&display=swap" rel="stylesheet">
<style>
:root{
  --orange:#f37122;
  --teal:#0d6e7e;
  --teal-dark:#0a5866;
  --navy:#123a44;
  --ink:#222;
  --body:#555;
  --light:#f2f2f2;
  --white:#fff;
}
*{box-sizing:border-box;margin:0;padding:0}
html,body{width:1200px;height:3249px;overflow:hidden}
body{font-family:"Roboto",sans-serif;color:var(--ink);background:var(--white);position:relative}
.abs{position:absolute}
.wrap{position:relative;width:1200px}

/* header */
.header{height:124px}
.brand{left:74px;top:22px;display:flex;flex-direction:column;align-items:flex-start;gap:8px}
.brand-mark{width:50px;height:50px;border-radius:50%;background:var(--orange)}
.brand-name{font-weight:700;font-size:17px;color:var(--teal);letter-spacing:1px;text-transform:uppercase}
.callus{left:760px;top:40px;display:flex;gap:12px;align-items:center}
.callus .icon{width:36px;height:36px;border-radius:50%;background:var(--orange);display:flex;align-items:center;justify-content:center}
.callus small{display:block;font-size:13px;color:#777}
.callus strong{font-size:18px;font-weight:500}
.club{left:980px;top:30px;width:150px;text-align:center;font-weight:700;font-size:17px;line-height:1.2;color:var(--ink);text-transform:uppercase}

/* nav */
.nav{height:43px;background:var(--teal);display:flex;align-items:stretch;padding-left:74px}
.nav a{color:var(--white);font-size:13px;font-weight:500;text-decoration:none;display:flex;align-items:center;padding:0 20px;text-transform:uppercase}
.nav a.active{background:var(--orange)}
.search{position:absolute;right:74px;top:6px;width:250px;height:31px;border-radius:16px;background:var(--white);display:flex;align-items:center;justify-content:space-between;padding:0 12px;font-size:12px;color:#999}

/* hero */
.hero{height:553px;overflow:hidden}
.hero-photo{inset:0;background:linear-gradient(100deg,#2f4726 0%,#56723f 30%,#8fa36a 52%,#e88a3a 72%,#f07a26 85%,#6e8450 100%)}
.hero-title{left:74px;top:172px;font-family:"Oswald",sans-serif;font-weight:500;font-size:58px;line-height:1;color:var(--white);text-transform:uppercase;letter-spacing:.5px}
.hero-text{left:74px;top:250px;width:420px;font-size:18px;line-height:1.5;color:var(--white);font-weight:500}
.btn{display:inline-block;background:var(--orange);color:var(--white);font-size:13px;font-weight:700;text-transform:uppercase;border-radius:22px;padding:14px 30px}
.hero .btn{position:absolute;left:74px;top:336px}
.dots{left:74px;top:507px;display:flex;gap:6px}
.dots span{width:10px;height:10px;border-radius:50%;background:rgba(255,255,255,.6)}
.dots span:first-child{background:var(--navy)}

/* welcome */
.welcome{height:421px}
.welcome h2{position:absolute;left:74px;top:50px;font-size:25px;font-weight:500}
.welcome h2 span{color:var(--teal)}
.welcome p{position:absolute;left:74px;top:92px;width:500px;font-size:14px;line-height:1.72;color:var(--body)}
.welcome .btn{position:absolute;left:74px;top:302px}
.video{left:613px;top:55px;width:513px;height:312px;background:linear-gradient(180deg,#15191c 0%,#2a3330 50%,#4f7a3c 78%,#35572a 100%)}
.play{left:50%;top:50%;width:70px;height:50px;margin:-25px 0 0 -35px;border-radius:10px;background:var(--orange);display:flex;align-items:center;justify-content:center}

/* diagram */
.diagram{height:351px;background:linear-gradient(90deg,#0e4a58 0%,#1a6473 50%,#0e4a58 100%)}
.diagram h3{position:absolute;top:48px;width:100%;text-align:center;color:var(--white);font-size:23px;font-weight:500}
.pillar{width:190px;height:190px;top:110px}
.pillar svg{position:absolute;inset:0}
.pillar span{position:absolute;inset:0;display:flex;align-items:center;justify-content:center;text-align:center;color:var(--white);font-size:17px;font-weight:500;line-height:1.25}

/* feature cards */
.features{height:580px}
.card{top:58px;width:513px;height:466px;border:1px solid #e3e3e3;background:var(--white);text-align:center}
.card .photo{height:314px}
.card h4{margin-top:30px;font-size:17px;font-weight:500}
.card p{margin:12px auto 0;width:455px;font-size:13.5px;line-height:1.75;color:var(--body)}
.card p a{color:var(--orange);text-decoration:none}

/* testimonial */
.testimonial{height:433px;background:var(--light)}
.testimonial .photo{left:596px;top:0;width:604px;height:433px;background:linear-gradient(90deg,#eef0ef 0%,#e2d3c4 35%,#c99a7c 55%,#f3f2ee 75%,#7ea0bf 100%)}
.testimonial h3{position:absolute;left:217px;top:47px;font-size:22px;font-weight:500}
.quote{left:100px;top:130px;width:420px;text-align:center;font-size:14px;line-height:1.75;color:var(--body)}
.quote .mark{color:var(--teal);font-size:34px;font-weight:700;line-height:0;vertical-align:-10px}
.quote cite{display:block;margin-top:12px;color:var(--orange);font-style:normal;font-size:17px}

/* tiles */
.tiles{height:442px}
.tile{top:57px;width:332px;height:331px}
.tile .label{position:absolute;left:0;right:0;top:260px;height:30px;background:rgba(255,255,255,.88);display:flex;align-items:center;justify-content:center;font-size:17px;font-weight:500}

/* footer */
.footer{height:262px;background:var(--teal);color:var(--white)}
.footer .mark{left:74px;top:60px;width:56px;height:56px;border-radius:50%;border:3px solid var(--white)}
.fcol{top:50px}
.fcol h5{font-size:16px;font-weight:500;margin-bottom:20px}
.fcol li{list-style:none;font-size:13px;line-height:1.55}
.fcol p{font-size:13px;line-height:1.6}
.email{width:243px;height:42px;background:var(--white);color:#999;font-size:13px;display:flex;align-items:center;padding-left:14px;margin-bottom:12px}
.subscribe{width:243px;height:38px;background:var(--orange);font-size:13px;font-weight:700;display:flex;align-items:center;justify-content:space-between;padding:0 14px;text-transform:uppercase}
.bottom{height:37px;background:var(--teal-dark);color:var(--white);font-size:13px;display:flex;align-items:center;justify-content:space-between;padding:0 74px}
.social{display:flex;gap:14px}
.social span{width:14px;height:14px;border-radius:50%;background:var(--white)}
</style>
</head>
<body>

<header class="wrap header">
  <div class="abs brand"><span class="brand-mark"></span><span class="brand-name">Bright Stride</span></div>
  <div class="abs callus">
    <span class="icon"><svg width="18" height="18" viewBox="0 0 24 24"><path fill="#fff" d="M6.6 10.8a15 15 0 0 0 6.6 6.6l2.2-2.2c.3-.3.7-.4 1-.2 1.1.4 2.3.6 3.6.6.6 0 1 .4 1 1V20c0 .6-.4 1-1 1A17 17 0 0 1 3 4c0-.6.4-1 1-1h3.5c.6 0 1 .4 1 1 0 1.3.2 2.5.6 3.6.1.3 0 .7-.2 1z"/></svg></span>
    <div><small>Call Us Today!</small><strong>1800 555 0147</strong></div>
  </div>
  <div class="abs club">Marrowby Field<br>Soccer Club</div>
</header>

<nav class="wrap nav">
  <a class="active">Home</a><a>Water</a><a>Fruits &amp; Vegetables</a><a>Stretch</a><a>Fuel Your Body</a><a>Protect Your Skin</a>
  <div class="search">Search<svg width="14" height="14" viewBox="0 0 24 24"><circle cx="10" cy="10" r="7" fill="none" stroke="#0d6e7e" stroke-width="3"/><path d="M15 15l6 6" stroke="#0d6e7e" stroke-width="3"/></svg></div>
</nav>

<section class="wrap hero">
  <div class="abs hero-photo" role="img" aria-label="Boy in an orange jersey drinking from a water bottle outdoors, holding a soccer ball"></div>
  <h1 class="abs hero-title">Drink More Water</h1>
  <p class="abs hero-text">Water is the single most critical nutrient in your body, and the most vital one we consume.</p>
  <span class="btn">Learn More</span>
  <div class="abs dots"><span></span><span></span><span></span><span></span><span></span></div>
</section>

<section class="wrap welcome">
  <h2>Welcome to <span>Bright Stride</span></h2>
  <p>Bright Stride is a partnership between Marrowby Field Soccer Club and the Northgate Foundation. It is an initiative to help communities develop attitudes and skills to make consistent and positive health related choices. Promote healthy child development through involvement in sports, building a sense of well-being and meeting the growth, development, and activity needs of healthy, confident children and young people. A health and wellness initiative that will educate and provide resources to the players and their families in Marrowby Field Soccer Club.</p>
  <span class="btn">Learn More</span>
  <div class="abs video" role="img" aria-label="Video still of a youth soccer team gathered with their coach on a floodlit field">
    <div class="abs play"><svg width="22" height="24" viewBox="0 0 22 24"><path d="M2 1l19 11L2 23z" fill="#fff"/></svg></div>
  </div>
</section>

<section class="wrap diagram">
  <h3>Bright Stride Diagram</h3>
  <div class="abs pillar" style="left:80px"><svg viewBox="0 0 190 190"><circle cx="95" cy="95" r="86" fill="none" stroke="#0f8797" stroke-width="11"/><circle cx="95" cy="95" r="86" fill="none" stroke="#f37122" stroke-width="11" stroke-dasharray="270 600" transform="rotate(180 95 95)"/></svg><span>Drink More<br>Water</span></div>
  <div class="abs pillar" style="left:249px"><svg viewBox="0 0 190 190"><circle cx="95" cy="95" r="86" fill="none" stroke="#0f8797" stroke-width="11"/><circle cx="95" cy="95" r="86" fill="none" stroke="#f37122" stroke-width="11" stroke-dasharray="270 600"/></svg><span>Fuel Your<br>Body</span></div>
  <div class="abs pillar" style="left:418px"><svg viewBox="0 0 190 190"><circle cx="95" cy="95" r="86" fill="none" stroke="#0f8797" stroke-width="11"/><circle cx="95" cy="95" r="86" fill="none" stroke="#f37122" stroke-width="11" stroke-dasharray="270 600" transform="rotate(180 95 95)"/></svg><span>Stretch<br>More</span></div>
  <div class="abs pillar" style="left:589px"><svg viewBox="0 0 190 190"><circle cx="95" cy="95" r="86" fill="none" stroke="#0f8797" stroke-width="11"/><circle cx="95" cy="95" r="86" fill="none" stroke="#f37122" stroke-width="11" stroke-dasharray="270 600"/></svg><span>Protect Your<br>Skin</span></div>
  <div class="abs pillar" style="left:760px"><svg viewBox="0 0 190 190"><circle cx="95" cy="95" r="86" fill="none" stroke="#0f8797" stroke-width="11"/><circle cx="95" cy="95" r="86" fill="none" stroke="#f37122" stroke-width="11" stroke-dasharray="270 600" transform="rotate(180 95 95)"/></svg><span>Move<br>More</span></div>
  <div class="abs pillar" style="left:932px"><svg viewBox="0 0 190 190"><circle cx="95" cy="95" r="86" fill="none" stroke="#0f8797" stroke-width="11"/><circle cx="95" cy="95" r="86" fill="none" stroke="#f37122" stroke-width="11" stroke-dasharray="270 600"/></svg><span>Sports<br>Mindset</span></div>
</section>

<section class="wrap features">
  <article class="abs card" style="left:74px">
    <div class="photo" role="img" aria-label="Youth players in navy kits drinking from water bottles on a grass field" style="background:linear-gradient(180deg,#9cc173 0%,#6f9a52 25%,#244a86 50%,#1f3f72 75%,#4a7a34 100%)"></div>
    <h4>Drink More Water</h4>
    <p>Water is the single most critical nutrient in your body, and the most vital one we consume. The human brain is composed of 95% water, blood is 82% water... <a>[MORE +]</a></p>
  </article>
  <article class="abs card" style="left:613px">
    <div class="photo" role="img" aria-label="Athlete in a blue jacket leaping in mid-air against a bright sky" style="background:linear-gradient(180deg,#dfe4e8 0%,#c7d3e6 35%,#f6f2e2 60%,#9a9c9c 85%,#6e7070 100%)"></div>
    <h4>Pillar and "Mindset"</h4>
    <p>Reference site about Lorem Ipsum, giving information on its origins, as well as a random Lipsum generator.Reference site about Lorem its Lipsum generator... <a>[MORE +]</a></p>
  </article>
</section>

<section class="wrap testimonial">
  <div class="abs photo" role="img" aria-label="Woman in athletic wear eating a fresh salad beside an exercise ball"></div>
  <h3>Happy Customer</h3>
  <blockquote class="abs quote">
    <span class="mark">“</span> Lorem Ipsum is simply dummy text of the printing and typesetting industry. Lorem Ipsum has been the industry's standard dummy text ever since the 1500s, when an unknown printer took a galley of type and scrambled it to make a type specimen book. It has survived not only five centuries, but also the leap into electronic typesetting, remaining essentially unchanged. <span class="mark">”</span>
    <cite>- Marisol</cite>
  </blockquote>
</section>

<section class="wrap tiles">
  <div class="abs tile" style="left:74px" role="img" aria-label="Young woman drinking from a water bottle after a workout"><div style="position:absolute;inset:0;background:linear-gradient(180deg,#ece4d8 0%,#d9b4a0 40%,#c8485a 75%,#a04a44 100%)"></div><div class="label">Performance and Hydration</div></div>
  <div class="abs tile" style="left:433px" role="img" aria-label="Colourful assortment of fresh fruits and berries"><div style="position:absolute;inset:0;background:linear-gradient(135deg,#b9c94a 0%,#d83a3a 40%,#5b2a55 65%,#e0a33a 100%)"></div><div class="label">Boost Performance by Adding Color</div></div>
  <div class="abs tile" style="left:793px" role="img" aria-label="Runner kneeling on a road checking her armband tracker"><div style="position:absolute;inset:0;background:linear-gradient(180deg,#f3ead9 0%,#d6c3a2 45%,#9a8a78 75%,#6e665c 100%)"></div><div class="label">Fuel Your Performance</div></div>
</section>

<footer class="wrap footer">
  <span class="abs mark"></span>
  <div class="abs fcol" style="left:225px">
    <h5>Contact Info</h5>
    <p>Bright Stride<br>228, Lorem ipsum dolor,<br>Street Area, ipsum - 54895</p>
    <p style="margin-top:16px">1800 555 0147<br>info@brightstridewithtown.example</p>
  </div>
  <div class="abs fcol" style="left:496px">
    <h5>Quick Links</h5>
    <ul><li>Home</li><li>Water</li><li>Fruits &amp; Vegetables</li><li>Stretch</li><li>Fuel Your Body</li><li>Protect Your Skin</li></ul>
  </div>
  <div class="abs fcol" style="left:719px">
    <h5>Company</h5>
    <ul><li>Terms of Use</li><li>Privacy Policy</li><li>Sitemap</li><li>Blog</li></ul>
  </div>
  <div class="abs fcol" style="left:883px">
    <h5>Subscribe Newsletter!</h5>
    <div class="email">Email Address</div>
    <div class="subscribe">Subscribe<svg width="22" height="14" viewBox="0 0 22 14"><rect x="1" y="1" width="20" height="12" fill="none" stroke="#fff" stroke-width="1.5"/><path d="M1 1l10 7 10-7" fill="none" stroke="#fff" stroke-width="1.5"/></svg></div>
  </div>
</footer>
<div class="wrap bottom"><span>© 2017 Bright Stride</span><div class="social"><span></span><span></span></div></div>

</body>
</html>
```